Business Card/Letterhead for Construction Company
Ronald Pike Construction
Professional
Ronald P. Pike
5702 Meadowlark Court, Suite #4
Millbrook, CO 80517
ronald@ronaldpikeconstruction.example
www.ronaldpikeconstruction.example
Possibly add Facebook page:
www.friendpages.example/pikehouses
Navy Logo
Main Logo

```html
<!DOCTYPE html>
<html lang="en">
<head>
<meta charset="utf-8">
<title>Ronald Pike Construction – Business Card</title>
<link rel="stylesheet" href="https://fonts.googleapis.com/css2?family=Cormorant+SC:wght@500;600;700&family=Cinzel:wght@600&display=swap">
<style>
  :root {
    --page-bg: #e9eaec;
    --card-bg: #ffffff;
    --navy: #1f3a68;
    --steel: #8d9298;
    --mist: #cfd2d6;
    --ink: #4f545b;
  }
  * { margin: 0; padding: 0; box-sizing: border-box; }
  html, body { width: 1200px; height: 1009px; overflow: hidden; }
  body {
    background: var(--page-bg);
    display: flex;
    flex-direction: column;
    align-items: center;
    justify-content: center;
    gap: 44px;
    font-family: "Cormorant SC", Georgia, serif;
    color: var(--ink);
  }
  .card {
    position: relative;
    width: 800px;
    height: 457px;
    background: var(--card-bg);
    border-radius: 24px;
    overflow: hidden;
    box-shadow: 0 6px 18px rgba(0,0,0,.12);
  }
  .brand {
    display: flex;
    align-items: center;
    gap: 14px;
  }
  .brand-dot {
    width: 34px; height: 34px;
    border-radius: 50%;
    background: var(--navy);
  }
  .brand-name {
    font-family: "Cinzel", Georgia, serif;
    font-weight: 600;
    color: var(--navy);
    letter-spacing: 1px;
    white-space: nowrap;
  }
  /* front */
  .card-front { display: flex; align-items: center; justify-content: center; }
  .card-front .brand-name { font-size: 34px; }
  .card-front .brand-dot { width: 46px; height: 46px; }
  /* back */
  .card-back .brand { position: absolute; left: 0; right: 0; top: 62px; justify-content: center; }
  .card-back .brand-name { font-size: 26px; }
  .holder {
    position: absolute; right: 430px; top: 172px;
    text-align: right;
    white-space: nowrap;
  }
  .holder-name { font-size: 26px; font-weight: 700; color: var(--ink); letter-spacing: .5px; }
  .holder-address { margin-top: 10px; font-size: 17px; font-weight: 500; line-height: 1.45; }
  .divider {
    position: absolute; left: 395px; top: 170px;
    width: 1px; height: 112px;
    background: var(--mist);
  }
  .contacts {
    position: absolute; left: 415px; top: 168px;
    list-style: none;
    font-size: 16px; font-weight: 600;
    white-space: nowrap;
  }
  .contacts li { display: flex; align-items: center; gap: 10px; height: 29px; }
  .contacts svg { flex: none; }
  .base-band {
    position: absolute; left: 0; right: 0; bottom: 0;
    height: 110px;
    background: linear-gradient(180deg, var(--mist) 0%, var(--steel) 35%, var(--navy) 75%);
  }
</style>
</head>
<body>
  <section class="card card-front">
    <div class="brand">
      <span class="brand-dot"></span>
      <span class="brand-name">RONALD PIKE CONSTRUCTION</span>
    </div>
  </section>

  <section class="card card-back">
    <div class="brand">
      <span class="brand-dot"></span>
      <span class="brand-name">RONALD PIKE CONSTRUCTION</span>
    </div>

    <div class="holder">
      <p class="holder-name">Ronald P. Pike</p>
      <p class="holder-address">5702 Meadowlark Court, Suite #4<br>Millbrook, CO 80517</p>
    </div>

    <span class="divider"></span>

    <ul class="contacts">
      <li>
        <svg width="18" height="18" viewBox="0 0 18 18"><circle cx="9" cy="9" r="9" fill="#8d9298"/><path d="M6 5l2 2-1 1.2c.6 1.2 1.6 2.2 2.8 2.8L11 10l2 2-1.2 1.3C8.6 13 5 9.4 4.7 6.2z" fill="#fff"/></svg>
        555-013-2048
      </li>
      <li>
        <svg width="18" height="18" viewBox="0 0 18 18"><circle cx="9" cy="9" r="9" fill="#8d9298"/><path d="M6 5l2 2-1 1.2c.6 1.2 1.6 2.2 2.8 2.8L11 10l2 2-1.2 1.3C8.6 13 5 9.4 4.7 6.2z" fill="#fff"/></svg>
        555-017-6310
      </li>
      <li>
        <svg width="18" height="18" viewBox="0 0 18 18"><circle cx="9" cy="9" r="9" fill="#8d9298"/><rect x="4.5" y="6" width="9" height="6.5" fill="none" stroke="#fff" stroke-width="1.2"/><path d="M4.5 6l4.5 3.6L13.5 6" fill="none" stroke="#fff" stroke-width="1.2"/></svg>
        ronald@ronaldpikeconstruction.example
      </li>
      <li>
        <svg width="18" height="18" viewBox="0 0 18 18"><circle cx="9" cy="9" r="9" fill="#8d9298"/><circle cx="9" cy="9" r="4.5" fill="none" stroke="#fff" stroke-width="1.2"/><path d="M4.5 9h9M9 4.5c-2 2.4-2 6.6 0 9M9 4.5c2 2.4 2 6.6 0 9" fill="none" stroke="#fff" stroke-width="1"/></svg>
        www.ronaldpikeconstruction.example
      </li>
    </ul>

    <div class="base-band" role="img" aria-label="Decorative layered band in light gray, gray and navy along the bottom edge"></div>
  </section>
</body>
</html>
```